Business Card Design

My company is an online based training service targeted at individuals who want to learn how to consistently make money at online tournament poker.

The training takes place online using skype and is extremely easy to use.

Final design should communicate that my business offers online tournament poker coaching from one of the most successful online tournament poker players in Scotland and the UK.

Further information can be found @ http://www.mendmyhand.net/

Industry/Entity Type

Training

Contact Information for Business Card

- 'Learn from one of the best online tournament poker players in Scotland and the UK' (or something similar)
- Previous winnings
Reference: http://www.mendmyhand.net/

Requirements
Must have
• MendMyHand.net
Nice to have
• A similar look or feel to my website (http://www.mendmyhand.net/)

```html
<!DOCTYPE html>
<html lang="en">
<head>
<meta charset="utf-8">
<title>Mend My Hand – Business Card</title>
<link rel="stylesheet" href="https://fonts.googleapis.com/css2?family=Gelasio:wght@500&family=Tinos&display=swap">
<style>
  :root {
    --ink-dark: #1c1d1f;
    --ink-mid: #4a4d52;
    --smoke-light: #e6ebef;
    --smoke-mid: #9aa3ab;
    --white: #ffffff;
    --photo-warm: #8a5a48;
    --photo-dark: #2a2527;
  }
  html, body {
    margin: 0;
    padding: 0;
    width: 1200px;
    height: 791px;
    overflow: hidden;
    background: var(--ink-dark);
  }
  .card {
    position: relative;
    width: 1200px;
    height: 791px;
    overflow: hidden;
    background:
      radial-gradient(ellipse 520px 420px at 1020px 300px, rgba(230,235,239,0.85), rgba(230,235,239,0) 70%),
      radial-gradient(ellipse 700px 300px at 1100px 80px, rgba(240,244,247,0.9), rgba(240,244,247,0) 70%),
      radial-gradient(ellipse 500px 260px at 700px 360px, rgba(154,163,171,0.45), rgba(154,163,171,0) 70%),
      linear-gradient(100deg, var(--ink-dark) 0%, #2c2e31 35%, var(--ink-mid) 60%, var(--smoke-mid) 85%, var(--smoke-light) 100%);
  }
  .brand-name {
    position: absolute;
    left: 62px;
    top: 104px;
    margin: 0;
    font-family: "Tinos", serif;
    font-weight: 400;
    font-size: 88px;
    line-height: 1;
    color: var(--white);
    white-space: nowrap;
  }
  .tagline {
    position: absolute;
    left: 136px;
    top: 204px;
    margin: 0;
    font-family: "Tinos", serif;
    font-size: 34px;
    line-height: 1;
    color: var(--white);
    white-space: nowrap;
  }
  .pitch {
    position: absolute;
    left: 78px;
    top: 328px;
    margin: 0;
    font-family: "Gelasio", serif;
    font-weight: 500;
    font-size: 34px;
    line-height: 44px;
    color: var(--white);
    white-space: nowrap;
  }
  .website {
    position: absolute;
    left: 86px;
    top: 613px;
    margin: 0;
    font-family: "Gelasio", serif;
    font-weight: 500;
    font-size: 32px;
    line-height: 1;
    color: var(--white);
    text-decoration: none;
  }
  .players-photo {
    position: absolute;
    left: 693px;
    top: 335px;
    width: 462px;
    height: 410px;
  }
</style>
</head>
<body>
  <main class="card">
    <h1 class="brand-name">Mend My Hand</h1>
    <p class="tagline">TAKE YOUR GAME TO THE NEXT LEVEL</p>
    <p class="pitch">
      &nbsp;online tournament poker coaching<br>
      from one of the most successful<br>
      online tournament poker players<br>
      in Scotland and the UK
    </p>
    <a class="website" href="http://www.mendmyhand.net/">MendMyHand.net</a>
    <svg class="players-photo" viewBox="0 0 462 410" role="img" aria-label="Photo of two poker players, a man in a suit holding chips and a woman holding playing cards, with poker chips in the foreground">
      <defs>
        <radialGradient id="photoTone" cx="60%" cy="55%" r="60%">
          <stop offset="0%" stop-color="#8a5a48" stop-opacity="0.9"/>
          <stop offset="100%" stop-color="#2a2527" stop-opacity="0.85"/>
        </radialGradient>
      </defs>
      <path d="M70 410 C60 300 90 140 170 90 C230 60 260 20 330 10 C420 0 460 120 455 230 C452 320 440 380 430 410 Z" fill="url(#photoTone)"/>
    </svg>
  </main>
</body>
</html>
```